Pull Up Banner Design 85cm X200cm

The pull up banner is intended for branding and services awareness purposes, and to be used at exhibition and conference. Please refer to the websites below for more information
1. https://www.advisory-nook.net/
2. https://www.advisory-nook.net/landing-page
3. https://blog.advisory-nook.net/faq-for-client/
4. https://blog.advisory-nook.net/faq-for-advisor/

Ideally, the banner will lead potential users both young entrepreneurs and online business owners (as clients) to Brivana Hub marketplace, and also professional services providers like accountants and finance advisors and consultants (as advisors) to sign up with the platform. (Like ArtForge marketplace)

Target Market(s)

Business users and accountants aged between 25 to 44 yrs old

Requirements
Must have
• website address (www.advisory-nook.net)
• and
• company logo "Brivana Hub" as attached

```html
<!DOCTYPE html>
<html lang="en">
<head>
<meta charset="utf-8">
<title>Brivana Hub – Pull Up Banner</title>
<link rel="stylesheet" href="https://fonts.googleapis.com/css2?family=Montserrat:wght@700&family=Bebas+Neue&family=Titillium+Web:wght@600;700&display=swap">
<style>
  :root {
    --stage: #b9babd;
    --blue: #1478c2;
    --blue-deep: #0f6db4;
    --blue-light: #3d9ad8;
    --teal-pale: #cfeeed;
    --teal: #8fd3d6;
    --tag-blue: #bfe6f5;
    --white: #ffffff;
    --charcoal: #333536;
    --slate: #4a4c50;
    --url-blue: #1b7fc8;
  }
  * { box-sizing: border-box; margin: 0; padding: 0; }
  html, body { width: 1200px; height: 1200px; overflow: hidden; }
  body { background: var(--stage); position: relative; font-family: "Titillium Web", sans-serif; }

  .banner {
    position: absolute; left: 345px; top: 0; width: 510px; height: 1200px;
    background: var(--blue); overflow: hidden; color: var(--white);
  }
  .banner > * { position: absolute; }
  .hero-backdrop { left: 0; top: 0; width: 510px; height: 340px; }

  .logo { left: 22px; top: 22px; display: flex; flex-direction: column; align-items: center; }
  .logo-mark { width: 42px; height: 42px; border-radius: 50%; background: var(--blue-deep); }
  .logo-name { margin-top: 6px; font-family: "Montserrat", sans-serif; font-weight: 700; font-size: 26px; color: var(--blue-deep); line-height: 1; }

  .headline {
    left: 0; width: 510px; top: 232px; text-align: center;
    font-family: "Montserrat", sans-serif; font-weight: 700; font-size: 54px; line-height: 1;
  }
  .headline .accent { color: var(--slate); }
  .tagline {
    left: 0; width: 510px; top: 303px; text-align: center;
    font-family: "Bebas Neue", sans-serif; font-size: 30px; color: var(--tag-blue); letter-spacing: .2px;
  }

  .section-title {
    left: 24px; font-family: "Bebas Neue", sans-serif; font-size: 34px; line-height: 1;
    white-space: nowrap; font-weight: 400;
  }
  .section-title.long { font-size: 30px; letter-spacing: 0; }
  .section-sub { left: 24px; width: 400px; font-weight: 700; font-size: 13px; line-height: 16.8px; text-transform: uppercase; }
  .section-sub.wide { width: 470px; }
  .intro { left: 24px; top: 386px; width: 462px; font-weight: 700; font-size: 12.8px; line-height: 16.8px; text-transform: uppercase; }
  .rule { left: 24px; width: 432px; height: 1px; background: var(--tag-blue); }

  .feature { left: 24px; width: 470px; display: flex; gap: 10px; }
  .feature-icon { flex: none; width: 54px; height: 54px; border-radius: 50%; background: var(--teal); margin-top: 14px; }
  .feature-title { font-weight: 600; font-size: 17px; line-height: 18px; text-transform: uppercase; color: var(--tag-blue); }
  .feature-body { font-weight: 600; font-size: 13.2px; line-height: 16.8px; color: var(--tag-blue); }

  .steps { left: 24px; width: 470px; list-style: none; }
  .steps li { position: absolute; left: 0; width: 450px; padding-left: 18px; font-weight: 600; font-size: 13.2px; line-height: 16.8px; color: var(--tag-blue); }
  .steps .num { position: absolute; left: 0; top: -3px; font-weight: 700; font-size: 16px; color: var(--tag-blue); }

  .footer { left: 0; top: 1080px; width: 510px; height: 120px; background: var(--charcoal); }
  .footer svg { position: absolute; left: 0; top: 0; }
  .globe { left: 235px; top: 1097px; }
  .site-url {
    left: 0; width: 510px; top: 1144px; text-align: center;
    font-family: "Bebas Neue", sans-serif; font-size: 34px; color: var(--url-blue);
  }
</style>
</head>
<body>
<main class="banner">
  <svg class="hero-backdrop" viewBox="0 0 510 340">
    <defs>
      <linearGradient id="bannerTop" x1="0" y1="0" x2="0" y2="1">
        <stop offset="0" stop-color="#3d9ad8"/>
        <stop offset="1" stop-color="#1478c2"/>
      </linearGradient>
      <linearGradient id="sceneFill" x1="0" y1="0" x2="1" y2="1">
        <stop offset="0" stop-color="#d6f1f0"/>
        <stop offset="1" stop-color="#7fcfcf"/>
      </linearGradient>
    </defs>
    <rect width="510" height="340" fill="url(#bannerTop)"/>
    <polygon points="0,208 58,265 0,320" fill="var(--teal-pale)"/>
    <polygon points="510,208 452,265 510,320" fill="var(--teal-pale)"/>
    <path d="M0 0 H510 V40 C500 160 390 240 255 240 C120 240 10 160 0 40 Z" fill="url(#sceneFill)" role="img" aria-label="Illustration: a smiling advisor at a laptop on a desk, connected by network lines to portraits of other advisors"/>
  </svg>

  <div class="logo">
    <span class="logo-mark"></span>
    <span class="logo-name">Brivana Hub</span>
  </div>

  <h1 class="headline">Brivana <span class="accent">Hub</span></h1>
  <p class="tagline">Matches you with the right advisors online!</p>

  <h2 class="section-title" style="top:352px">What is Brivana Hub?</h2>
  <p class="intro">Brivana Hub is where we find the best business advisors and professionals for you! Our platform helps you overcome barriers to find and connect with the right advisors so that you won’t have to waste resources unnecessarily or worry about mismatches. We’ve made solving business problems a lot easier.</p>
  <div class="rule" style="top:478px"></div>

  <h2 class="section-title" style="top:486px">Why Brivana Hub?</h2>
  <p class="section-sub" style="top:518px">Discover and get matched with the right advisors and professionals</p>

  <div class="feature" style="top:554px">
    <span class="feature-icon" role="img" aria-label="Online shop storefront icon"></span>
    <div>
      <h3 class="feature-title">One-stop borderless marketplace</h3>
      <p class="feature-body">Access instantly to a network of great independent advisors, consultants, industry professionals, boutique firms and small sized practices, including best talents in accounting, finance and strategy all in one place.</p>
    </div>
  </div>

  <div class="feature" style="top:645px">
    <span class="feature-icon" role="img" aria-label="Running figure icon"></span>
    <div>
      <h3 class="feature-title">Convenient and quick</h3>
      <p class="feature-body">Get matched instantly to 3 of the great advisors for you to compare. Then communicate, chat, interview, appoint and sign the engagement online.</p>
    </div>
  </div>

  <div class="feature" style="top:724px">
    <span class="feature-icon" role="img" aria-label="Thumbs-up icon"></span>
    <div>
      <h3 class="feature-title">Hire with confidence</h3>
      <p class="feature-body">Explore each advisors profile and browse their previous works as well as clients review in a simple manner online.</p>
    </div>
  </div>

  <div class="rule" style="top:794px"></div>

  <h2 class="section-title long" style="top:802px">How does Brivana Hub work for advisors?</h2>
  <p class="section-sub wide" style="top:832px">We’ve made it as easy to use for advisors as it is for clients!</p>

  <ol class="steps" style="top:862px">
    <li style="top:0"><span class="num">1.</span>Sign-up, create your profile and upload your jobs portfolio.</li>
    <li style="top:28px"><span class="num">2.</span>Browse and apply for jobs posted by Clients. You can connect with them directly or more information and discuss terms.</li>
    <li style="top:68px"><span class="num">3.</span>Agree terms through an Engagement Letter and send your invoice directly to Clients.</li>
    <li style="top:108px"><span class="num">4.</span>Brivana Hub will charge you a Pay-Per-Job fee of 10% of your job earnings.</li>
    <li style="top:138px"><span class="num">5.</span>Update the progress of your job through your Dashboard.</li>
    <li style="top:166px"><span class="num">6.</span>When jobs are completed, Clients will give you reviews that will help boost your credibility and build your virtual brand.</li>
  </ol>

  <div class="footer">
    <svg width="510" height="120" viewBox="0 0 510 120" aria-hidden="true">
      <polygon points="0,8 58,60 0,120" fill="var(--blue-light)"/>
      <polygon points="0,120 58,60 110,120" fill="var(--blue)"/>
      <polygon points="510,8 452,60 510,120" fill="var(--blue-light)"/>
      <polygon points="510,120 452,60 400,120" fill="var(--blue)"/>
    </svg>
  </div>
  <svg class="globe" width="40" height="40" viewBox="0 0 40 40" aria-hidden="true">
    <g fill="none" stroke="#cfeeed" stroke-width="2.4">
      <circle cx="20" cy="20" r="18"/>
      <ellipse cx="20" cy="20" rx="8" ry="18"/>
      <line x1="2" y1="20" x2="38" y2="20"/>
      <line x1="5" y1="11" x2="35" y2="11"/>
      <line x1="5" y1="29" x2="35" y2="29"/>
    </g>
  </svg>
  <p class="site-url">www.advisory-nook.net</p>
</main>
</body>
</html>
```